Hoods and pressure washing

We pressure wash house, driveways, buisnesses, gas stations, restraunt hoods and equipments, fences, construction sites and anything that can be pressure washed

Will like my flyer to have written: licenesed, bonded, and insured up to 2 million.(but professionally written)

Target Market(s)

Restraunts, corporations, houses and apartment complexes

Industry/Entity Type

Construction

Colors
33a6d7
33b8a4
ffffff
3176b5

Requirements
Must have
• Before and after pics of dirty and clean pics
Nice to have
• I would like it to be a one paper flyer could be front or back. Company name is aquaBrite. I like a corner written down with all the work we do. Ex: hoods, sidewalks, sidings, houses etc...
• Contact info: Dennis Cawley, phone# 629-415-3307
• Lou Marten, phone # (didnt get one yet)
• Adress: 2417 E. Brantwood rd, portland, Tn, 37162

```html
<!DOCTYPE html>
<html lang="en">
<head>
<meta charset="utf-8">
<title>aquaBrite Pressure Washing Flyer</title>
<link href="https://fonts.googleapis.com/css2?family=Montserrat:wght@800&family=Arimo:wght@400;700&display=swap" rel="stylesheet">
<style>
  :root {
    --page-bg: #e6e6e6;
    --brand-blue: #3a96d6;
    --brand-blue-light: #4aa6e0;
    --teal: #52c4cc;
    --teal-band: #6fc9d0;
    --ring-grey: #c9cbcc;
    --white: #ffffff;
    --ink: #111111;
  }
  * { margin: 0; padding: 0; box-sizing: border-box; }
  html, body { width: 1069px; height: 1200px; overflow: hidden; background: var(--page-bg); }
  body { position: relative; font-family: "Arimo", Arial, sans-serif; }

  .flyer {
    position: absolute; left: 132px; top: 30px;
    width: 846px; height: 1200px;
    transform: scale(0.95); transform-origin: 0 0;
    background: var(--white); overflow: hidden;
  }
  .flyer > * { position: absolute; }

  .header {
    left: 0; top: 0; width: 846px; height: 270px;
    background: radial-gradient(circle at 640px 60px, var(--brand-blue-light) 0 180px, transparent 181px),
                radial-gradient(circle at 80px 330px, var(--brand-blue-light) 0 170px, transparent 171px),
                var(--brand-blue);
  }
  .brand-mark {
    left: 73px; top: 35px; width: 190px; height: 190px; border-radius: 50%;
    background: #2f5ea8; border: 4px solid var(--white);
  }
  .brand-name {
    left: 300px; top: 92px; color: var(--white);
    font-family: "Montserrat", Arial, sans-serif; font-weight: 800; font-size: 64px; letter-spacing: 1px;
  }
  .services-line {
    left: 303px; top: 166px; color: var(--white); font-size: 20px; letter-spacing: 0.3px;
  }

  .hero-photo {
    left: 0; top: 270px; width: 846px; height: 472px;
    background: linear-gradient(90deg, #3c3a36 0%, #5a5850 40%, #e9e9e9 42%, #e9e9e9 70%, #4f8a33 85%, #3f7a2a 100%);
  }
  .hero-photo::before {
    content: ""; position: absolute; left: 0; top: 0; width: 100%; height: 230px;
    background: linear-gradient(180deg, #cfd7dc 0%, #e8e2d4 60%, #d9d1c0 100%);
  }
  .hero-notch { left: 0; top: 270px; }
  .before-label, .after-label { font-weight: 700; font-size: 52px; }
  .hero-before { left: 78px; top: 668px; color: var(--white); text-shadow: 0 2px 3px rgba(0,0,0,.5); }
  .hero-after { left: 470px; top: 668px; color: var(--ink); }

  .insured-badge {
    left: 582px; top: 209px; width: 236px; height: 236px; border-radius: 50%;
    background: var(--teal); border: 10px solid var(--ring-grey);
    color: var(--white); text-align: center;
  }
  .badge-figure { font-family: "Montserrat", Arial, sans-serif; font-weight: 800; font-size: 96px; line-height: 86px; margin-top: 6px; }
  .badge-unit { font-weight: 700; font-size: 28px; line-height: 30px; letter-spacing: 1px; }
  .badge-copy { font-size: 21px; line-height: 24px; }

  .price-badge {
    left: 43px; top: 394px; width: 224px; height: 224px; border-radius: 50%;
    border: 8px solid var(--ring-grey); overflow: hidden;
    background: linear-gradient(180deg, #6b4b30 0%, #a8642e 55%, var(--teal) 55%);
    color: var(--white); text-align: center;
  }
  .price-lead { margin-top: 126px; font-weight: 700; font-size: 20px; }
  .price-amount { font-weight: 700; font-size: 36px; line-height: 38px; }

  .services-band {
    left: 0; top: 742px; width: 846px; height: 96px; background: var(--teal-band);
    color: var(--white); font-size: 20px; line-height: 24px; text-align: center; padding: 12px 50px 0;
  }

  .boardwalk-photo {
    left: 0; top: 845px; width: 418px; height: 355px;
    background: linear-gradient(180deg, #8c8f87 0%, #7d8078 50%, #c89a4a 56%, #b88636 100%);
  }
  .boardwalk-before { left: 0; width: 418px; top: 952px; text-align: center; color: var(--white); font-size: 38px; font-weight: 700; }
  .boardwalk-after { left: 0; width: 418px; top: 1098px; text-align: center; color: var(--white); font-size: 38px; font-weight: 700; }

  .contacts-panel {
    left: 428px; top: 845px; width: 418px; height: 355px;
    background: radial-gradient(circle at 460px 320px, var(--brand-blue-light) 0 150px, transparent 151px), var(--brand-blue);
    color: var(--white); text-align: center; padding-top: 50px;
  }
  .contacts-title { font-weight: 700; font-size: 35px; margin-bottom: 6px; }
  .contacts-line { font-size: 21px; line-height: 28.5px; }
</style>
</head>
<body>
  <main class="flyer">
    <header class="header"></header>
    <div class="brand-mark"></div>
    <div class="brand-name">aquaBrite</div>
    <div class="services-line">HOODS.SIDEWALKS.SIDINGS.HOUSES.ETC.</div>

    <div class="hero-photo" role="img" aria-label="Photo of a house driveway, dirty on the left half and pressure-washed clean on the right"></div>
    <svg class="hero-notch" width="846" height="24" viewBox="0 0 846 24" aria-hidden="true">
      <polygon points="385,0 461,0 423,22" fill="var(--brand-blue)"/>
    </svg>
    <div class="before-label hero-before">Before</div>
    <div class="after-label hero-after">After</div>

    <div class="price-badge">
      <div class="price-lead" role="img" aria-label="Close-up of a pressure washer nozzle cleaning a wooden deck">Price from</div>
      <div class="price-amount">$49.99</div>
    </div>

    <div class="insured-badge">
      <div class="badge-figure">2</div>
      <div class="badge-unit">MILLION</div>
      <div class="badge-copy">LICENESED,<br>BONDED,<br>AND<br>INSURED</div>
    </div>

    <p class="services-band">We pressure wash house, driveways, buisnesses, gas stations, restraunt hoods and equipments, fences, construction sites and anything that can be pressure washed</p>

    <div class="boardwalk-photo" role="img" aria-label="Wooden boardwalk, grey and weathered at the far end and freshly cleaned at the near end"></div>
    <div class="boardwalk-before">Before</div>
    <div class="boardwalk-after">After</div>

    <section class="contacts-panel">
      <h2 class="contacts-title">CONTACTS</h2>
      <p class="contacts-line">DENNIS CAWLEY,</p>
      <p class="contacts-line">PHONE# 629-415-3307</p>
      <p class="contacts-line">LOU MARTEN,</p>
      <p class="contacts-line">PHONE # 629-415-3307</p>
      <p class="contacts-line">ADRESS:</p>
      <p class="contacts-line">2417 E. BRANTWOOD RD,</p>
      <p class="contacts-line">PORTLAND, TN, 37162</p>
    </section>
  </main>
</body>
</html>
```